Business cards for Paperleaf Sprites

Please note that the color of the logo has been changed from green to teal blue. Sorry for the changing!

Anything will go but want to have some funky side.

I would like the front of the business card is the logo and business information and the back side is the Adult Coloring, so that would attract the customer to do the coloring on the other side. Have more interactive side. (pictures for references only can see it below). Fairies on the back of the card for coloring and whatever you want to adds on to color, like flowers, nature etc......

Scrapbooking is not just paper, it also involves watercolor, mixed media, art, all the fun stuff.

Another keypoint I would like to stress on is the back of the business card should be Adult Coloring and make sure you are not google and use the search engine to copy and paste because of the copyright issue.

As a designer, I am sure you all can create beautiful artwork.

Please submit your creativities!

Want the business card is out of the ordinary and customers would like to keep that as a keepsake rather than treat like a regular business card and trash it. Fonts cannot be too small, consider some of the customers have to wear bi-focal eyeglasses.

Thanks a lot!

Target Market(s)

Scrapbooking, Card making, papercraft, stampin‘ , gifts items , etc.

Industry/Entity Type

Retail

Contact Information for Business Card

Color Scheme, please match with the Logo. Watercolor effect is nice!
Thanks!

Font styles to use
Serif

Requirements
Must have
• I would like Elegant and playful.
• Thanks!
Nice to have
• Watercolor effect or check out the Adult Coloring Book, I am thinking we can use a double-sided business card, one side for the information and the other side for people can do the coloring. I have attached 2 pictures for reference.
Should not have
• No black color on the background please!

```html
<!DOCTYPE html>
<html lang="en">
<head>
<meta charset="utf-8">
<title>Paperleaf Sprites – Business Card</title>
<link rel="stylesheet" href="https://fonts.googleapis.com/css2?family=Bitter:wght@400;700&display=swap">
<style>
  :root {
    --page-bg: #d9d9d9;
    --card-bg: #fdfdf8;
    --teal: #3f93a3;
    --teal-dark: #2f7f8f;
    --red: #b8232f;
    --text-grey: #6b6b6b;
    --divider: #8a8a8a;
    --fairy-pink: #e77bbf;
    --fairy-blue: #8fd3e6;
    --butterfly-pink: #e85a8a;
    --butterfly-green: #b8d94a;
  }
  * { box-sizing: border-box; margin: 0; padding: 0; }
  html, body {
    width: 1200px; height: 1000px; overflow: hidden;
    background: var(--page-bg);
    font-family: "Bitter", Georgia, serif;
  }
  .business-card {
    position: absolute; left: 180px; top: 260px;
    width: 840px; height: 480px;
    background: var(--card-bg);
    border-radius: 34px;
    overflow: hidden;
    box-shadow: 0 10px 30px rgba(0,0,0,0.18);
  }
  .wave-bands { position: absolute; inset: 0; }
  .fairy-illustration {
    position: absolute; left: 110px; top: 18px;
    width: 150px; height: 120px; border-radius: 50%;
    background: radial-gradient(circle at 45% 45%, var(--fairy-pink) 0%, rgba(231,123,191,0.5) 40%, rgba(143,211,230,0.35) 65%, rgba(253,253,248,0) 75%);
  }
  .brand-name {
    position: absolute; left: 40px; top: 160px; width: 290px;
    text-align: center;
    font-size: 34px; font-weight: 700; line-height: 1.15;
    color: var(--teal);
  }
  .divider {
    position: absolute; left: 352px; top: 160px;
    width: 1.5px; height: 190px; background: var(--divider);
  }
  .contact-block { position: absolute; left: 382px; top: 140px; width: 430px; }
  .person-name { font-size: 40px; font-weight: 700; letter-spacing: 1px; line-height: 1; }
  .person-name .first { color: var(--teal); }
  .person-name .last { color: var(--red); }
  .person-title {
    font-size: 16px; font-weight: 700; color: var(--text-grey);
    letter-spacing: 0.5px; margin-top: 6px; margin-bottom: 16px;
  }
  .contact-list { list-style: none; }
  .contact-item {
    display: flex; align-items: flex-start; gap: 12px;
    font-size: 18px; font-weight: 700; color: var(--text-grey);
    line-height: 1.35; margin-bottom: 4px;
  }
  .contact-icon { width: 18px; height: 18px; flex: none; margin-top: 4px; fill: var(--text-grey); }
  .butterfly-illustration {
    position: absolute; left: 760px; top: 140px;
    width: 52px; height: 44px; border-radius: 40%;
    background: linear-gradient(90deg, var(--butterfly-pink), var(--butterfly-green) 55%, var(--fairy-blue));
  }
</style>
</head>
<body>
  <div class="business-card">
    <svg class="wave-bands" viewBox="0 0 840 480" width="840" height="480" aria-hidden="true">
      <path class="teal-wave" d="M0,222 C150,245 250,365 420,400 C600,432 740,442 840,446 L840,480 L0,480 Z" fill="var(--teal)"/>
      <path class="white-swoosh" d="M0,240 C140,262 240,355 390,404 C240,372 140,278 0,256 Z" fill="var(--card-bg)"/>
      <path class="red-swoosh" d="M390,386 C570,414 740,424 840,428 L840,438 C740,434 570,420 390,386 Z" fill="var(--red)"/>
    </svg>

    <div class="fairy-illustration" role="img" aria-label="Small watercolour fairy with wand and sparkles"></div>

    <div class="brand-name">Paperleaf Sprites</div>

    <div class="divider"></div>

    <div class="contact-block">
      <div class="person-name"><span class="first">CLARA</span> <span class="last">BENNING</span></div>
      <div class="person-title">PRESIDENT/OWNER</div>
      <ul class="contact-list">
        <li class="contact-item">
          <svg class="contact-icon" viewBox="0 0 24 24"><path d="M6.6 10.8a15 15 0 0 0 6.6 6.6l2.2-2.2a1 1 0 0 1 1-.25 11.4 11.4 0 0 0 3.6.57 1 1 0 0 1 1 1V20a1 1 0 0 1-1 1A17 17 0 0 1 3 4a1 1 0 0 1 1-1h3.5a1 1 0 0 1 1 1c0 1.25.2 2.45.57 3.6a1 1 0 0 1-.25 1z"/></svg>
          <span>+12-555-01842</span>
        </li>
        <li class="contact-item">
          <svg class="contact-icon" viewBox="0 0 24 24"><path d="M2 5h20v14H2z M2 5l10 8 10-8" fill="none" stroke="var(--text-grey)" stroke-width="2"/></svg>
          <span>clarabenning@mailbox.com</span>
        </li>
        <li class="contact-item">
          <svg class="contact-icon" viewBox="0 0 24 24"><circle cx="12" cy="12" r="9" fill="none" stroke="var(--text-grey)" stroke-width="2"/><path d="M3 12h18M12 3c3 3 3 15 0 18M12 3c-3 3-3 15 0 18" fill="none" stroke="var(--text-grey)" stroke-width="1.6"/></svg>
          <span>www.paperleafsprites.com</span>
        </li>
        <li class="contact-item">
          <svg class="contact-icon" viewBox="0 0 24 24"><path d="M12 2a7 7 0 0 0-7 7c0 5 7 13 7 13s7-8 7-13a7 7 0 0 0-7-7zm0 9.5A2.5 2.5 0 1 1 12 6.5a2.5 2.5 0 0 1 0 5z"/></svg>
          <span>Willow Creek Road Santa<br>Rosa, CA 95401, USA</span>
        </li>
      </ul>
    </div>

    <div class="butterfly-illustration" role="img" aria-label="Colourful patterned butterfly"></div>
  </div>
</body>
</html>
```